Bref créative
Dale's Furniture
Stationary, Letterhead, Business Cards, Envelopes
I need single sided standard sized Business Card [3.5" x 2"]
Similar to Logo Font
Bright & Fun-filled
Dale's Furniture and Appliances
4817 W. Corvel Ave.
Chicago IL 60688
Dalesfurnitureandappliances@quillmail.example
www.dalesfurnitureandapplianes.example
Current Logo
Black and White Version

```html
<!DOCTYPE html>
<html lang="en">
<head>
<meta charset="utf-8">
<title>Dale's Furniture — Stationery Set</title>
<link href="https://fonts.googleapis.com/css2?family=Cinzel:wght@700&family=Open+Sans:wght@400;600&display=swap" rel="stylesheet">
<style>
  :root{
    --backdrop:#8a8a8a;
    --paper:#ffffff;
    --ink:#2a2a2a;
    --muted:#6b6b6b;
    --red:#d4141b;
    --red-deep:#7a0508;
    --black:#111111;
    --window:#e4e4e4;
  }
  *{margin:0;padding:0;box-sizing:border-box}
  html,body{width:1200px;height:818px;overflow:hidden}
  body{background:var(--backdrop);position:relative;font-family:"Open Sans",Arial,sans-serif;color:var(--ink)}
  .sheet{position:absolute;background:var(--paper);box-shadow:0 2px 6px rgba(0,0,0,.35);overflow:hidden}
  .letterhead{left:65px;top:96px;width:494px;height:636px}
  .business-card{left:619px;top:96px;width:209px;height:115px;border-radius:8px}
  .envelope-back{left:578px;top:319px;width:560px;height:228px}
  .envelope-front{left:578px;top:564px;width:560px;height:168px}
  .band{position:absolute;left:0;bottom:0;width:100%}
  .brand{position:absolute;display:flex;flex-direction:column;align-items:flex-start}
  .brand-row{display:flex;align-items:center;gap:6px}
  .brand-mark{background:var(--red);display:block}
  .brand-name{font-family:"Cinzel",Georgia,serif;font-weight:700;color:var(--black);white-space:nowrap}
  .brand-tag{font-size:7px;letter-spacing:.5px;color:var(--muted);text-transform:uppercase;margin-top:3px;border-top:1px solid #999;padding-top:2px;white-space:nowrap}
  .contact{position:absolute;font-size:7px;line-height:11px;color:var(--muted)}
  .contact .accent{color:var(--red)}
  .web{position:absolute;font-size:7px;color:var(--muted)}
  .letterhead .brand{left:22px;top:30px}
  .letterhead .brand-mark{width:14px;height:14px}
  .letterhead .brand-name{font-size:17px}
  .letterhead .contact{left:380px;top:26px;width:100px}
  .letterhead .web{right:22px;bottom:26px}
  .business-card .brand{left:12px;top:22px}
  .business-card .brand-mark{width:8px;height:8px}
  .business-card .brand-name{font-size:9px}
  .business-card .brand-tag{font-size:4px;margin-top:2px}
  .card-details{position:absolute;right:10px;top:12px;width:92px;text-align:right}
  .card-name{font-size:8px;font-weight:600;color:var(--red);line-height:10px}
  .card-title{font-size:5px;color:var(--muted);line-height:7px}
  .card-contact{margin-top:22px;font-size:4.5px;line-height:7px;color:var(--muted)}
  .envelope-back .web{left:207px;top:16px;color:#fff;font-size:6px;z-index:2}
  .flap{position:absolute;left:0;top:0}
  .envelope-front .brand{left:12px;top:22px}
  .envelope-front .brand-mark{width:11px;height:11px}
  .envelope-front .brand-name{font-size:13px}
  .envelope-front .brand-tag{font-size:5px}
  .envelope-front .contact{left:12px;top:82px;font-size:5.5px;line-height:9px}
  .address-window{position:absolute;left:279px;top:48px;width:245px;height:72px;background:var(--window);border:1px solid #cfcfcf;border-radius:8px}
</style>
</head>
<body>
<svg width="0" height="0" style="position:absolute">
  <defs>
    <linearGradient id="band-fade" x1="0" x2="1" y1="0" y2="0">
      <stop offset="0" stop-color="#7a0508"/>
      <stop offset=".35" stop-color="#d4141b"/>
      <stop offset=".75" stop-color="#ff2a2a"/>
      <stop offset="1" stop-color="#d4141b"/>
    </linearGradient>
    <radialGradient id="flap-glow" cx=".5" cy=".1" r=".75">
      <stop offset="0" stop-color="#ff2e2e"/>
      <stop offset=".55" stop-color="#c40f15"/>
      <stop offset="1" stop-color="#3a0204"/>
    </radialGradient>
  </defs>
</svg>

<section class="sheet letterhead">
  <div class="brand">
    <div class="brand-row"><span class="brand-mark"></span><span class="brand-name">Dale's Furniture</span></div>
    <div class="brand-tag">Appliances and Home Furnishings</div>
  </div>
  <div class="contact">
    4817 W. Corvel Ave.<br>Chicago IL 60688<br><span class="accent">Tel.</span> 773.555.0148<br><span class="accent">Fax.</span> 773.555.0149
  </div>
  <div class="web">www.dalesfurnitureandapplianes.example</div>
  <svg class="band" viewBox="0 0 494 20" height="20" preserveAspectRatio="none">
    <rect x="0" y="8" width="494" height="12" fill="url(#band-fade)"/>
    <polygon points="360,8 494,8 494,20 372,20" fill="#111"/>
    <polygon points="352,4 358,4 370,20 364,20" fill="#fff"/>
  </svg>
</section>

<section class="sheet business-card">
  <div class="brand">
    <div class="brand-row"><span class="brand-mark"></span><span class="brand-name">Dale's Furniture</span></div>
    <div class="brand-tag">Appliances and Home Furnishings</div>
  </div>
  <div class="card-details">
    <div class="card-name">Dale's</div>
    <div class="card-title">Owner</div>
    <div class="card-contact">
      4817 W. Corvel Ave.<br>Chicago IL 60688<br>Tel. 773.555.0148<br>Dalesfurnitureandappliances@<br>quillmail.example
    </div>
  </div>
  <svg class="band" viewBox="0 0 209 14" height="14" preserveAspectRatio="none">
    <rect x="0" y="4" width="209" height="10" fill="url(#band-fade)"/>
    <polygon points="150,4 209,4 209,14 156,14" fill="#111"/>
    <polygon points="144,1 148,1 155,14 151,14" fill="#fff"/>
  </svg>
</section>

<section class="sheet envelope-back">
  <svg class="flap" width="560" height="228" viewBox="0 0 560 228">
    <path d="M0 0 H560 L330 176 Q280 200 230 176 Z" fill="url(#flap-glow)"/>
    <path d="M330 176 Q280 200 230 176" fill="none" stroke="#e9e9e9" stroke-width="2"/>
  </svg>
  <div class="web">www.dalesfurnitureandapplianes.example</div>
</section>

<section class="sheet envelope-front">
  <div class="brand">
    <div class="brand-row"><span class="brand-mark"></span><span class="brand-name">Dale's Furniture</span></div>
    <div class="brand-tag">Appliances and Home Furnishings</div>
  </div>
  <div class="contact">4817 W. Corvel Ave. Chicago IL 60688<br>Tel. 773.555.0148</div>
  <div class="address-window"></div>
  <svg class="band" viewBox="0 0 560 20" height="20" preserveAspectRatio="none">
    <rect x="0" y="8" width="560" height="12" fill="url(#band-fade)"/>
    <polygon points="380,8 560,8 560,20 392,20" fill="#111"/>
    <polygon points="370,2 376,2 390,20 384,20" fill="#fff"/>
  </svg>
</section>
</body>
</html>
```